Email & signature design template

My company sells photo ID and plastic card products. I would like a new email design template that reflects our focus on secure, smart, ID cards. Like your Government ID card, only with a bit more bling (colour). Using guilloche patterns and similar security feature design perhaps even hologram type effect from credit cards would be great. FOCUS ON THE SIGNATURE. No fancy background graphics making email hard to read. File size needs to be kept to a minimum and black and white email for possible printing is also preferred. Needs to include space for employee photo. Name, telephone number, optional mobile number and email address. As well as a reminder to save our trees and only print this email if absolutely necessary would be nice. Also space for ratings buttons and T&C's. I have attached our current design which I am not to fond of. Also a copy of a VERY old one which we liked much more but was impossible to automate with slanting text not being an option outside of making it part of an image. Traditionally our CI colours were orange and grey like that found on the logo copy attached. You are welcome to design complimentary to those colours. Hope that's good enough to let you have fun coming up with the proposals.

Target Market(s)

Business people in Government, IT and security markets.

Font styles to use
Serif

Colors
0692cd
0255a3
f04a50

Requirements
Must have
• Like your Government ID card, only with a bit more bling (colour). Using guilloche patterns and similar security feature design perhaps even hologram type effect from credit cards would be great. FOCUS ON THE SIGNATURE.
• employee photo. Name, telephone number, optional mobile number and email address.
Nice to have
• As well as a reminder to save our trees and only print this email if absolutely necessary would be nice.
• hologram type effect from credit cards would be great.
Should not have
• Text at angles.
• Dark or difficult background for main email layout to make it difficult to read.
• Signature can be any colours. Still be easy to read.

```html
<!DOCTYPE html>
<html lang="en">
<head>
<meta charset="utf-8">
<title>Email Signature – Keystone Card Services</title>
<link rel="stylesheet" href="https://fonts.googleapis.com/css2?family=Special+Elite&family=Open+Sans:ital,wght@0,400;0,600;0,700;1,700&display=swap">
<style>
  :root {
    --paper: #ffffff;
    --paper-tint: #ececec;
    --card-dark: #1b1b1b;
    --card-mid: #3a3a3a;
    --card-edge: #555555;
    --photo-grey: #d9d9d9;
    --ink: #111111;
    --white: #ffffff;
    --orange: #f7941d;
    --grey: #8c8c8c;
    --grey-dark: #6d6d6d;
    --gold: #f5b81c;
    --gold-edge: #b07a0a;
    --footer-dark: #111111;
    --footer-mid: #262626;
  }
  * { margin: 0; padding: 0; box-sizing: border-box; }
  html, body { width: 1200px; height: 406px; overflow: hidden; background: var(--paper); }

  .signature {
    position: relative;
    width: 1200px;
    height: 406px;
    background: var(--paper);
    font-family: "Open Sans", Arial, sans-serif;
  }

  .security-backdrop {
    position: absolute;
    left: 0; top: 0;
    width: 1200px; height: 311px;
    background: linear-gradient(180deg, var(--paper) 0%, var(--paper-tint) 55%, var(--paper) 100%);
    opacity: 0.6;
  }

  /* ID card */
  .id-card {
    position: absolute;
    left: 24px; top: 26px;
    width: 398px; height: 258px;
    border-radius: 14px;
    overflow: hidden;
    background: var(--card-dark);
  }
  .id-card__texture {
    position: absolute; inset: 0;
    background: linear-gradient(135deg, var(--card-mid) 0%, var(--card-dark) 40%, var(--card-edge) 62%, var(--card-dark) 100%);
  }
  .id-card__photo {
    position: absolute;
    left: 24px; top: 56px;
    width: 93px; height: 115px;
    background: var(--photo-grey);
  }
  .id-card__brand {
    position: absolute;
    right: 20px; top: 16px;
    display: flex; align-items: center; gap: 5px;
    font-family: "Open Sans", Arial, sans-serif;
    font-weight: 700;
    font-size: 20px;
    color: var(--photo-grey);
    letter-spacing: 1px;
  }
  .brand-square { width: 9px; height: 9px; background: var(--orange); }
  .id-card__name {
    position: absolute;
    left: 141px; top: 60px;
    font-family: "Special Elite", "Courier New", monospace;
    font-size: 23px;
    letter-spacing: 2.5px;
    color: var(--white);
    text-transform: uppercase;
  }
  .id-card__contacts {
    position: absolute;
    left: 166px; top: 96px;
    list-style: none;
    font-family: "Special Elite", "Courier New", monospace;
    font-size: 12.5px;
    line-height: 17.5px;
    color: var(--orange);
    letter-spacing: 0.6px;
  }
  .id-card__reminder {
    position: absolute;
    left: 12px; top: 227px;
    font-family: "Special Elite", "Courier New", monospace;
    font-size: 9px;
    letter-spacing: 0.5px;
    color: var(--white);
    text-transform: uppercase;
  }

  .divider {
    position: absolute;
    left: 682px; top: 23px;
    width: 2px; height: 258px;
    background: var(--ink);
  }

  /* Company block */
  .company {
    position: absolute;
    left: 900px; top: 12px;
    width: 296px;
    text-align: center;
  }
  .company__mark {
    display: inline-flex; align-items: center; gap: 8px;
    height: 70px;
    font-weight: 700;
    font-size: 42px;
    color: var(--grey);
    letter-spacing: 1px;
  }
  .company__mark .brand-square { width: 14px; height: 14px; }
  .company__web {
    margin-top: 8px;
    font-size: 12.5px;
    letter-spacing: 3.4px;
    color: var(--orange);
    text-transform: uppercase;
  }
  .company__tagline {
    margin-top: 5px;
    font-size: 16.5px;
    line-height: 22px;
    font-weight: 700;
    font-style: italic;
    color: var(--grey);
    text-transform: uppercase;
  }

  /* Rating */
  .rating {
    position: absolute;
    left: 924px; top: 206px;
    width: 248px; height: 83px;
    border: 2px solid var(--ink);
    background: var(--white);
  }
  .rating__title {
    height: 30px;
    background: var(--ink);
    color: var(--white);
    font-size: 16px;
    letter-spacing: 4.2px;
    text-align: center;
    line-height: 30px;
    text-transform: uppercase;
  }
  .rating__scale {
    display: flex; align-items: center; justify-content: center;
    height: 49px;
    gap: 1px;
  }

  /* Footer */
  .legal {
    position: absolute;
    left: 0; top: 311px;
    width: 1200px; height: 95px;
  }
  .legal__texture {
    position: absolute; inset: 0;
    background: linear-gradient(180deg, var(--footer-mid) 0%, var(--footer-dark) 100%);
  }
  .legal__content {
    position: relative;
    padding: 24px 36px 0 36px;
  }
  .legal__title {
    font-size: 10.5px;
    font-weight: 600;
    color: var(--orange);
    text-transform: uppercase;
    margin-bottom: 1px;
  }
  .legal__text {
    font-family: Arial, "Open Sans", sans-serif;
    font-size: 10.6px;
    line-height: 14px;
    color: var(--white);
  }
</style>
</head>
<body>
<main class="signature">
  <div class="security-backdrop" role="img" aria-label="Faint guilloche security line pattern"></div>

  <section class="id-card" aria-label="Employee ID card">
    <div class="id-card__texture" role="img" aria-label="Dark carbon fibre card texture"></div>
    <div class="id-card__photo" role="img" aria-label="Employee photo"></div>
    <div class="id-card__brand"><span class="brand-square"></span>KCS</div>
    <h1 class="id-card__name">Marten Visser</h1>
    <ul class="id-card__contacts">
      <li>+27 (0)087 240 5512</li>
      <li>+27 (0)11 734 6620</li>
      <li>marten@kcs.co.za</li>
      <li>www.keystonecard.co.za</li>
    </ul>
    <p class="id-card__reminder">Save our trees and only print this email if absolutely necessary</p>
  </section>

  <div class="divider"></div>

  <section class="company">
    <div class="company__mark"><span class="brand-square"></span>KCS</div>
    <p class="company__web">www.keystonecard.co.za</p>
    <p class="company__tagline">Keystone Card<br>Services</p>
  </section>

  <section class="rating">
    <div class="rating__title">Rate my service</div>
    <div class="rating__scale">
      <svg width="34" height="40" viewBox="0 0 34 40" aria-label="Thumbs down">
        <path d="M4 3h9v20H4z M13 4h11c3 0 4 2 4 4l2 10c0 3-2 5-5 5h-6l2 8c0 3-2 5-4 5l-4-13z" fill="none" stroke="#111" stroke-width="2.2" stroke-linejoin="round"/>
      </svg>
      <svg width="150" height="30" viewBox="0 0 150 30" aria-label="Five stars">
        <defs>
          <polygon id="star" points="15,1 19,11 29.5,11.5 21.5,18 24,28.5 15,22.5 6,28.5 8.5,18 0.5,11.5 11,11" fill="#f5b81c" stroke="#b07a0a" stroke-width="1"/>
        </defs>
        <use href="#star" x="0"/>
        <use href="#star" x="30"/>
        <use href="#star" x="60"/>
        <use href="#star" x="90"/>
        <use href="#star" x="120"/>
      </svg>
      <svg width="34" height="40" viewBox="0 0 34 40" aria-label="Thumbs up">
        <path d="M21 17h9v20h-9z M21 36H10c-3 0-4-2-4-4L4 22c0-3 2-5 5-5h6l-2-8c0-3 2-5 4-5l4 13z" fill="none" stroke="#111" stroke-width="2.2" stroke-linejoin="round"/>
      </svg>
    </div>
  </section>

  <footer class="legal">
    <div class="legal__texture" role="img" aria-label="Dark hexagon pattern band"></div>
    <div class="legal__content">
      <h2 class="legal__title">Disclaimer</h2>
      <p class="legal__text">The information contained in this communication is confidential and may be legally privileged. It is intended soley for use by intended receipient and others authorized to receive it. If you are not the intended or authorized to receive it, any disclosure, copying, distribution or reliance of the contents of this information is strictly prohibited.</p>
    </div>
  </footer>
</main>
</body>
</html>
```